Note/Card sent to show appreciation to partners who worked with us to improve local communities

I'd like a simple note/card designed for a wide audience. Originally, I called this a "Thanksgiving Card," but it's really just a card to be sent around Thanksgiving, not specifically celebrating the Thanksgiving holiday. We plan to send the card out just prior to Thanksgiving 2017 (Nov. 24, 2017). I work at a regulated electric utility, and we'd like to say thank you to the many stakeholders who we partner with throughout the year to support initiatives that help to improve our state and create opportunities for economic growth. I'm interested mostly in the design of the card, not the simple verbiage on the inside.
Customers, charitable foundations, nonprofits, advocacy groups, industry associations, friends

```html
<!DOCTYPE html>
<html lang="en">
<head>
<meta charset="utf-8">
<title>Thanks card – Brightfield Power</title>
<link rel="stylesheet" href="https://fonts.googleapis.com/css2?family=Libre+Caslon+Text:wght@400&display=swap">
<style>
  :root {
    --backdrop: #e4e7ee;
    --card-orange: #ec922a;
    --card-orange-deep: #e3861e;
    --panel-purple: #643190;
    --ink-white: #ffffff;
    --faint-white: rgba(255, 255, 255, 0.2);
  }
  * { box-sizing: border-box; margin: 0; padding: 0; }
  html, body {
    width: 1200px;
    height: 768px;
    overflow: hidden;
    background: var(--backdrop);
  }
  .card {
    position: relative;
    width: 1200px;
    height: 768px;
    overflow: hidden;
    background: linear-gradient(160deg, var(--card-orange) 0%, var(--card-orange-deep) 100%);
    font-family: "Libre Caslon Text", Georgia, serif;
  }
  .card__sheen {
    position: absolute;
    inset: 0;
    width: 1200px;
    height: 768px;
  }
  .brand {
    position: absolute;
    left: 520px;
    top: 96px;
    display: flex;
    align-items: center;
    gap: 14px;
    color: var(--ink-white);
    font-size: 30px;
    font-weight: 400;
    letter-spacing: 0.5px;
    white-space: nowrap;
  }
  .brand__dot {
    flex: none;
    width: 22px;
    height: 22px;
    border-radius: 50%;
    background: var(--ink-white);
  }
  .brand--faint {
    left: 24px;
    top: 530px;
    font-size: 64px;
    line-height: 1.05;
    gap: 22px;
    color: var(--faint-white);
  }
  .brand--faint .brand__dot {
    width: 52px;
    height: 52px;
    background: var(--faint-white);
  }
  .thanks-panel {
    position: absolute;
    left: 500px;
    top: 200px;
    width: 470px;
    height: 420px;
    background: var(--panel-purple);
    overflow: hidden;
    display: flex;
    align-items: center;
    justify-content: center;
  }
  .thanks-panel__glow {
    position: absolute;
    inset: 0;
    width: 470px;
    height: 420px;
  }
  .thanks-panel__word {
    position: relative;
    color: var(--ink-white);
    font-size: 132px;
    font-weight: 400;
    letter-spacing: -1px;
    line-height: 1;
    margin-top: 20px;
  }
</style>
</head>
<body>
  <main class="card">
    <svg class="card__sheen" viewBox="0 0 1200 768" aria-hidden="true">
      <path d="M960 0 C1060 200 1080 470 980 768 L1200 768 L1200 0 Z" fill="rgba(255,255,255,0.12)"/>
      <path d="M900 0 C1010 220 1030 480 930 768" fill="none" stroke="rgba(255,255,255,0.35)" stroke-width="6"/>
      <path d="M1010 0 C1110 210 1120 470 1030 768" fill="none" stroke="rgba(255,255,255,0.22)" stroke-width="40"/>
    </svg>

    <div class="brand brand--faint" aria-hidden="true">
      <span class="brand__dot"></span>
      <span class="brand__name">Brightfield<br>Power</span>
    </div>

    <div class="brand">
      <span class="brand__dot"></span>
      <span class="brand__name">Brightfield Power</span>
    </div>

    <section class="thanks-panel">
      <svg class="thanks-panel__glow" viewBox="0 0 470 420" aria-hidden="true">
        <path d="M330 0 C420 130 380 320 180 420 L470 420 L470 0 Z" fill="rgba(255,255,255,0.13)"/>
      </svg>
      <h1 class="thanks-panel__word">thanks</h1>
    </section>
  </main>
</body>
</html>
```